Contemporary Creative Innovative Furniture Store & Online

We need a series of quarter page ads which we will run each week in a small colour magazine. Our idea is to promote a different product/designer each week in the ad. We provide Australian custom made statement pieces - our design or the clients. Only limited by imagination. The first ads to be designed 1) blinds - custom made own designs or designs in existence 2) custom made furniture 3) Danish designed sofa beds. Information on the product can be taken from www.quellmorestudiocbr.com.au - bespoke furniture has the tove lumen pieces (ie chairs) Corvel has the sofa beds. Images can be sent if required. We need readers to understand that not only can they source pieces from our online store, we can create and design individual pieces of furniture ie occasional chairs, dining chairs, soft furnishings including blinds and not at ridiculous prices. Service is friendly professional and personalised. Once the look of the ad is finalised and chosen, they must be produced to the specs we will provide as given by the magazine.
More images can be supplied if necessary. This will be ongoing work for the successful designer.

Target Market(s)

our market will appeal to 30s plus and anywhere from there

Industry/Entity Type

Furniture Store

Requirements
Must have
• Company logo, opening times of business, phone number, address
Nice to have
• ads to be interesting colourful and vibrant and modern
Should not have
• not too much writing - no block letters

```html
<!DOCTYPE html>
<html lang="en">
<head>
<meta charset="UTF-8">
<title>Quellmore Studio – Quarter Page Ad</title>
<link rel="stylesheet" href="https://fonts.googleapis.com/css2?family=Didact+Gothic&family=Poiret+One&display=swap">
<style>
  :root {
    --brown-deep: #2e170b;
    --brown-mid: #4a2714;
    --brown-glow: #5e331b;
    --lime: #c6d600;
    --white: #ffffff;
    --page: #d9d9d9;
    --upholstery: #3f3d5c;
    --timber: #7a4620;
  }
  * { margin: 0; padding: 0; box-sizing: border-box; }
  html, body {
    width: 1200px;
    height: 738px;
    overflow: hidden;
    background: var(--page);
  }
  .ad {
    position: relative;
    width: 1200px;
    height: 738px;
    overflow: hidden;
    background: radial-gradient(ellipse at 70% 40%, var(--brown-glow) 0%, var(--brown-mid) 40%, var(--brown-deep) 100%);
    color: var(--white);
  }
  .ad__backdrop {
    position: absolute;
    inset: 0;
    width: 100%;
    height: 100%;
  }
  .ad__product-photo {
    position: absolute;
    left: 60px;
    top: 225px;
    width: 620px;
    height: 490px;
    border-radius: 40% 46% 8% 10% / 30% 34% 6% 8%;
    background: radial-gradient(ellipse at 45% 40%, #7b7a96 0%, var(--upholstery) 55%, var(--timber) 100%);
  }
  .brand {
    position: absolute;
    left: 690px;
    top: 150px;
    width: 480px;
    display: flex;
    align-items: center;
    gap: 18px;
    font-family: "Didact Gothic", Arial, sans-serif;
    font-size: 62px;
    line-height: 1;
    color: var(--white);
    letter-spacing: 0.5px;
  }
  .brand__dot {
    flex: 0 0 auto;
    width: 22px;
    height: 22px;
    border-radius: 50%;
    background: var(--lime);
  }
  .tagline {
    position: absolute;
    left: 745px;
    top: 350px;
    width: 420px;
    font-family: "Didact Gothic", Arial, sans-serif;
    font-size: 21px;
    letter-spacing: 0.3px;
    text-align: left;
    white-space: nowrap;
  }
  .hours {
    position: absolute;
    left: 880px;
    top: 405px;
    width: 300px;
    text-align: center;
    font-family: "Didact Gothic", Arial, sans-serif;
  }
  .hours__days { font-size: 34px; line-height: 1.2; }
  .hours__time { font-size: 44px; line-height: 1.15; }
  .contact {
    position: absolute;
    left: 760px;
    top: 640px;
    width: 400px;
    text-align: center;
    font-family: "Didact Gothic", Arial, sans-serif;
  }
  .contact__phone { font-size: 46px; letter-spacing: 2px; line-height: 1.1; }
  .contact__web { font-size: 24px; letter-spacing: 0.3px; }
</style>
</head>
<body>
  <main class="ad">
    <svg class="ad__backdrop" viewBox="0 0 1200 738" preserveAspectRatio="none" aria-hidden="true">
      <g fill="none" stroke="#ffffff" stroke-opacity="0.06" stroke-width="2">
        <path d="M520 738 C700 520 900 380 1200 330"/>
        <path d="M600 738 C760 560 960 450 1200 420"/>
        <path d="M700 0 C820 160 980 230 1200 250"/>
        <path d="M880 0 C960 120 1080 170 1200 180"/>
      </g>
      <path class="ad__swoosh-lime" d="M0 66 C240 20 560 60 705 215 C520 120 260 95 0 120 Z" fill="var(--lime)"/>
      <path class="ad__swoosh-white" d="M0 96 C270 70 560 120 705 215 C780 380 700 620 560 738 L0 738 Z" fill="var(--white)"/>
    </svg>

    <div class="ad__product-photo" role="img" aria-label="Photo of a pair of occasional armchairs with curved timber arms and patterned upholstery"></div>

    <div class="brand">
      <span class="brand__dot"></span>
      <span class="brand__name">quellmore studio</span>
    </div>

    <p class="tagline">DESIGNER LOOKS AT ONLINE PRICES</p>

    <div class="hours">
      <p class="hours__days">Thur &amp; Fri</p>
      <p class="hours__time">10am-3pm</p>
    </div>

    <div class="contact">
      <p class="contact__phone">0491 570 156</p>
      <p class="contact__web">www.quellmorestudiocbr.com.au</p>
    </div>
  </main>
</body>
</html>
```